Fahrzeugbeschriftung für Brandschutzservice
Zielgruppe
Siehe bitte www.lorventa.de
Aufgabenstellung
Brandschutzservice / Kundendienst / Feuerlöscher vor Ort beim Kunden prüfen /

```html
<!DOCTYPE html>
<html lang="de">
<head>
<meta charset="utf-8">
<title>Kelberger Brandschutzservice – Fahrzeugbeschriftung</title>
<link rel="stylesheet" href="https://fonts.googleapis.com/css2?family=Open+Sans:wght@400;700&display=swap">
<style>
  :root {
    --canvas-bg: #eef0f2;
    --panel: #ffffff;
    --ink: #1f1f1f;
    --brand-red: #d8232a;
    --flame-deep: #e2561a;
    --flame-mid: #f08a1c;
    --flame-light: #f7c23a;
    --band-start: #e07a14;
    --band-end: #e9c83c;
  }
  * { margin: 0; padding: 0; box-sizing: border-box; }
  html, body { width: 1200px; height: 800px; overflow: hidden; }
  body {
    background: var(--canvas-bg);
    font-family: "Open Sans", Arial, sans-serif;
    color: var(--ink);
  }
  .wrap-panel {
    position: absolute;
    left: 40px; top: 60px;
    width: 1120px; height: 680px;
    background: var(--panel);
    overflow: hidden;
  }
  .flame-art {
    position: absolute;
    left: 0; top: 0;
    width: 520px; height: 680px;
  }
  .brand {
    position: absolute;
    left: 330px; top: 70px;
    display: flex;
    align-items: flex-start;
    gap: 22px;
  }
  .brand-square {
    width: 74px; height: 74px;
    background: var(--brand-red);
    margin-top: 6px;
  }
  .brand-name {
    font-weight: 700;
    font-size: 34px;
    line-height: 1.15;
  }
  .brand-services {
    list-style: none;
    margin-top: 8px;
    font-size: 24px;
    line-height: 1.3;
  }
  .slogan {
    position: absolute;
    left: 500px; top: 360px;
    font-weight: 700;
    font-size: 54px;
    line-height: 1.12;
    letter-spacing: 0.5px;
  }
  .slogan span { display: block; }
  .slogan .step-2 { padding-left: 60px; }
  .slogan .step-3 { padding-left: 130px; }
  .contact-band {
    position: absolute;
    left: 330px; top: 580px;
    width: 790px; height: 62px;
    background: linear-gradient(90deg, var(--band-start), var(--band-end));
    display: flex;
    align-items: center;
    justify-content: space-between;
    padding: 0 28px;
    font-weight: 700;
    font-size: 32px;
  }
</style>
</head>
<body>
  <div class="wrap-panel">
    <svg class="flame-art" viewBox="0 0 520 680" role="img" aria-label="Flammenmotiv in Orange und Gelb, das von links über die Fläche züngelt">
      <defs>
        <linearGradient id="flameGrad" x1="0" y1="0" x2="1" y2="1">
          <stop offset="0" stop-color="var(--flame-deep)"/>
          <stop offset="0.5" stop-color="var(--flame-mid)"/>
          <stop offset="1" stop-color="var(--flame-light)"/>
        </linearGradient>
      </defs>
      <path d="M0 0 H170 C230 80 200 180 260 260 C320 330 300 420 380 480 C440 530 470 600 500 680 H0 Z"
            fill="url(#flameGrad)" opacity="0.9"/>
    </svg>

    <div class="brand">
      <div class="brand-square"></div>
      <div class="brand-text">
        <div class="brand-name">Kelberger<br>Brandschutzservice</div>
        <ul class="brand-services">
          <li>Feuerlöschtechnik</li>
          <li>Löschanlagen</li>
          <li>Service &amp; Zubehör</li>
        </ul>
      </div>
    </div>

    <div class="slogan">
      <span class="step-1">BERATUNG</span>
      <span class="step-2">VERKAUF</span>
      <span class="step-3">SERVICE</span>
    </div>

    <div class="contact-band">
      <span class="contact-phone">Tel. : 03641 / 47 19 62</span>
      <span class="contact-web">www.lorventa.de</span>
    </div>
  </div>
</body>
</html>
```